Disposable Mini Sauce Pot Design for Asian Chain Food Brands

We operate a Hainan Chicken Rice takeout brand under the name Wokly8, with our official website: www.Wokly8.com.
We offer four signature house sauces and are launching brand-new packaging for our sauce line. We require custom graphic designs exclusively for the sauce cup lids.
Product Material & Base Specs
The sauce cups are made of PP plastic, available in two translucent base options: Translucent White and Translucent Orange.
Four Sauce Varieties for Individual Lid Designs
1. Red Sauce – Fried Sweet Chili Sauce
2.Green Sauce – Scallion Oil Dressing
3.Sweet Soy Sauce
4.Sweet Red Sauce (Special for Fried Chicken)
Differentiate each sauce lid design through unique graphics, typography, or illustrative elements for easy customer identification.
The marking NET WT 2 OZ must be clearly printed on every lid.
**There is no need to print full descriptive text or the full name of the sauces on each lid; the design only needs to clearly differentiate the four sauce varieties.
**Please reference the original design style and brand color palette shown on our official website, and feel free to fully unleash your creativity.
Look and feel
Each slider illustrates characteristics of the customer's brand and the style your logo design should communicate.

```html
<!DOCTYPE html>
<html lang="en">
<head>
<meta charset="utf-8">
<title>Wokly8 Sauce Lid Labels</title>
<link rel="stylesheet" href="https://fonts.googleapis.com/css2?family=Bebas+Neue&family=Arimo:wght@400;700&display=swap">
<style>
  :root {
    --page: #ffffff;
    --ink: #ffffff;
    --chili-light: #f6a21a;
    --chili-dark: #c8520a;
    --scallion-light: #a6c81c;
    --scallion-dark: #3f6a12;
    --soy-light: #7a3a12;
    --soy-dark: #4a1e08;
    --red-light: #c8241e;
    --red-dark: #7e0c0c;
  }
  * { box-sizing: border-box; margin: 0; padding: 0; }
  html, body { width: 912px; height: 1200px; overflow: hidden; background: var(--page); }
  .sheet {
    width: 912px; height: 1200px;
    display: flex; flex-direction: column; align-items: center; justify-content: center;
    gap: 34px;
  }
  .lid-label {
    position: relative; width: 340px; height: 254px; overflow: hidden;
    color: var(--ink);
  }
  .lid-label__pattern { position: absolute; inset: 0; }
  .lid-label--chili .lid-label__pattern { background: radial-gradient(ellipse at 60% 45%, var(--chili-light) 30%, var(--chili-dark) 100%); }
  .lid-label--scallion .lid-label__pattern { background: radial-gradient(ellipse at 60% 45%, var(--scallion-light) 35%, var(--scallion-dark) 100%); }
  .lid-label--soy .lid-label__pattern { background: radial-gradient(ellipse at 60% 45%, var(--soy-light) 30%, var(--soy-dark) 100%); }
  .lid-label--red .lid-label__pattern { background: radial-gradient(ellipse at 60% 45%, var(--red-light) 35%, var(--red-dark) 100%); }

  .sauce-name {
    position: absolute; font-family: "Bebas Neue", sans-serif; font-weight: 400;
    line-height: 0.86; letter-spacing: 0.5px;
  }
  .sauce-name span { display: block; }
  .brand {
    position: absolute; right: 28px; top: 26px; text-align: left;
    font-family: "Bebas Neue", sans-serif;
  }
  .brand__name { display: block; font-size: 38px; line-height: 0.9; letter-spacing: 1px; }
  .brand__tag { display: block; font-family: "Arimo", sans-serif; font-weight: 700; font-size: 6.5px; letter-spacing: 0.6px; }
  .ingredients {
    position: absolute; left: 178px; width: 136px;
    font-family: "Arimo", sans-serif;
  }
  .ingredients__title { font-size: 7.5px; font-weight: 700; margin-bottom: 2px; }
  .ingredients__text { font-size: 4.6px; line-height: 1.25; }
  .net-wt {
    position: absolute; left: 204px;
    font-family: "Arimo", sans-serif; font-weight: 700; font-size: 10.5px; letter-spacing: 0.2px;
  }
  .tagline {
    position: absolute; font-family: "Bebas Neue", sans-serif; font-size: 17px; line-height: 0.95;
  }
  .vertical-word {
    position: absolute; font-family: "Bebas Neue", sans-serif; font-size: 62px; line-height: 1;
    transform: rotate(-90deg); transform-origin: left top; letter-spacing: 0.5px;
  }
</style>
</head>
<body>
<main class="sheet">

  <section class="lid-label lid-label--chili">
    <div class="lid-label__pattern" role="img" aria-label="Chili pepper illustration pattern on orange"></div>
    <h2 class="sauce-name" style="left:24px; top:26px; font-size:58px;">
      <span>Fried</span><span>Sweet</span><span>Chili</span><span>Sauce</span>
    </h2>
    <div class="brand"><span class="brand__name">Wokly8</span><span class="brand__tag">HAINAN CHICKEN</span></div>
    <div class="ingredients" style="top:180px;">
      <p class="ingredients__title">Ingredients:</p>
      <p class="ingredients__text">Red chili, cane sugar, rice vinegar, garlic, water, salt, modified corn starch, fried shallot, sesame oil. Keep refrigerated after opening.</p>
    </div>
    <p class="net-wt" style="top:222px;">NET WT 2 OZ</p>
  </section>

  <section class="lid-label lid-label--scallion">
    <div class="lid-label__pattern" role="img" aria-label="Scallion illustration pattern on green"></div>
    <h2 class="vertical-word" style="left:26px; top:218px;">Scallion</h2>
    <p class="sauce-name" style="left:76px; top:34px; font-size:70px;">
      <span>Oil</span><span>Dres</span><span>sing</span>
    </p>
    <div class="brand"><span class="brand__name">Wokly8</span><span class="brand__tag">HAINAN CHICKEN</span></div>
    <div class="ingredients" style="top:174px; left:196px; width:120px;">
      <p class="ingredients__title">Ingredients:</p>
      <p class="ingredients__text">Scallion, vegetable oil, fresh ginger, salt, sugar, white pepper, sesame oil, garlic. Shake well before use. Keep refrigerated after opening.</p>
    </div>
    <p class="net-wt" style="top:222px; left:212px;">NET WT 2 OZ</p>
  </section>

  <section class="lid-label lid-label--soy">
    <div class="lid-label__pattern" role="img" aria-label="Soybean pod illustration pattern on brown"></div>
    <h2 class="sauce-name" style="left:24px; top:36px; font-size:70px;">
      <span>Sweet</span><span>Soy</span><span>Sauce</span>
    </h2>
    <div class="brand" style="right:22px; top:40px;"><span class="brand__name">Wokly8</span><span class="brand__tag">HAINAN CHICKEN</span></div>
    <div class="ingredients" style="top:168px; left:200px; width:118px;">
      <p class="ingredients__title">Ingredients:</p>
      <p class="ingredients__text">Water, soy sauce, palm sugar, molasses, salt, garlic, star anise, ginger, sesame oil. Shake well before use. Keep refrigerated after opening.</p>
    </div>
    <p class="net-wt" style="top:222px; left:212px;">NET WT 2 OZ</p>
  </section>

  <section class="lid-label lid-label--red">
    <div class="lid-label__pattern" role="img" aria-label="Chicken and flower illustration pattern on red"></div>
    <h2 class="sauce-name" style="left:22px; top:34px; font-size:74px;">
      <span>Sweet</span><span>Red</span><span>Sauce</span>
    </h2>
    <p class="tagline" style="left:128px; top:118px;">Special for<br>Fried Chicken</p>
    <div class="brand" style="right:26px; top:30px;"><span class="brand__name">Wokly8</span><span class="brand__tag">HAINAN CHICKEN</span></div>
    <div class="ingredients" style="top:170px; left:200px; width:120px;">
      <p class="ingredients__title">Ingredients:</p>
      <p class="ingredients__text">Red chili, tomato, cane sugar, garlic, rice vinegar, salt, paprika, water, lime juice. Shake well before use. Keep refrigerated after opening.</p>
    </div>
    <p class="net-wt" style="top:222px; left:212px;">NET WT 2 OZ</p>
  </section>

</main>
</body>
</html>
```